Minimalistic and chic product labels required for tea packaging

We need a Label Sticker Design for our tea company that is minimalistic, simple and chic.

We have 2 categories of tea: artisan tea (single flavoured tea e.g. green and black) and herbal teas (e.g. mixuture of herbs and flowers). We would like to have the designs to tell the difference of artisan tea and herbal tea, this can be done by having different colours to tell the difference or if there are other design features used.

We would also like to have colourful colours on our herbal tea range, preferably either a light and chic pastel colour palette or bright and chic colour palette.

The labels will be stuck onto a white pouch. The final design should also include the variety of colour palettes that can be used in AI format with the label. Preferred label measurements in 9cm width, and 11cm height. Our logo is attached.

Target Market(s)

Beauty and wellness

Industry/Entity Type

Health And Wellness

Requirements
Must have
• 2 x labels (front and back)
Front label must include logo, text to include tea type and weight
Back label must include text space to write description
Nice to have
• Simple and chic label design to stick onto a white pouch
Should not have
• Must not have too much graphic and pictures

```html
<!DOCTYPE html>
<html lang="en">
<head>
<meta charset="utf-8">
<title>Verdale Artisan Tea – Front and Back Labels</title>
<link rel="stylesheet" href="https://fonts.googleapis.com/css2?family=Josefin+Sans:wght@300;400&family=Special+Elite&family=Libre+Franklin:wght@400;800;900&display=swap">
<style>
  :root {
    --stage: #a0a890;
    --label-sand: #e6ddca;
    --label-sand-deep: #d8cdb5;
    --leaf-green: #8db23c;
    --leaf-green-light: #a6c455;
    --leaf-green-dark: #6e9128;
    --emblem-green: #4f7f24;
    --ink: #1c1c1c;
    --paper: #ffffff;
    --soft-white: rgba(255,255,255,0.85);
  }
  * { box-sizing: border-box; margin: 0; padding: 0; }
  html, body { width: 1200px; height: 835px; overflow: hidden; }
  body { background: var(--stage); position: relative; font-family: "Josefin Sans", sans-serif; }

  .label {
    position: absolute; top: 190px; width: 460px; height: 460px;
    background: linear-gradient(90deg, var(--label-sand-deep) 0%, var(--label-sand) 18%, var(--label-sand) 82%, var(--label-sand-deep) 100%);
    overflow: hidden;
  }
  .label--front { left: 110px; }
  .label--back { left: 630px; }

  .leaf-decor {
    position: absolute; right: 0; top: 110px; width: 200px; height: 300px;
    background: radial-gradient(ellipse at 60% 40%, rgba(255,255,255,0.28), rgba(255,255,255,0) 70%);
  }

  .pennant {
    position: absolute; background: var(--leaf-green);
    display: flex; flex-direction: column; align-items: center; justify-content: center;
  }
  .label--front .pennant {
    left: 135px; top: 0; width: 190px; height: 170px; padding-bottom: 40px;
    clip-path: polygon(0 0, 100% 0, 100% 72%, 50% 100%, 0 72%);
  }
  .label--back .pennant {
    left: 0; top: 0; width: 210px; height: 175px; padding-bottom: 55px;
    clip-path: polygon(0 0, 100% 0, 100% 70%, 0 100%);
  }
  .brand-name {
    font-family: "Josefin Sans", sans-serif; font-weight: 300; font-size: 28px;
    color: var(--paper); letter-spacing: 2px;
    border-top: 1px solid var(--soft-white); border-bottom: 1px solid var(--soft-white);
    padding: 8px 16px 4px;
  }

  .emblem {
    position: absolute; width: 42px; height: 42px; border-radius: 50%;
    background: var(--emblem-green);
  }
  .label--front .emblem { left: 209px; top: 178px; }
  .label--back .emblem { left: 60px; top: 145px; }

  .type-band {
    position: absolute; display: flex; flex-direction: column; align-items: center; justify-content: center;
    background: linear-gradient(90deg, var(--leaf-green-dark), var(--leaf-green-light) 25%, var(--leaf-green-light) 75%, var(--leaf-green-dark));
  }
  .label--front .type-band { left: 12px; right: 12px; top: 222px; height: 48px; }
  .label--back .type-band { left: 210px; right: 0; top: 35px; height: 46px; }
  .type-name { font-weight: 400; font-size: 27px; letter-spacing: 7px; color: var(--ink); line-height: 1; padding-top: 4px; }
  .label--back .type-name { font-size: 24px; letter-spacing: 6px; }
  .type-sub { font-weight: 300; font-size: 12px; letter-spacing: 3px; color: #3e4a28; line-height: 1; }

  .tea-name-frame {
    position: absolute; left: 48px; right: 48px; top: 290px; height: 66px;
    border: 1.5px solid var(--leaf-green);
    display: flex; align-items: center; justify-content: center;
  }
  .placeholder-text {
    font-family: "Special Elite", monospace; color: var(--paper); letter-spacing: 6px;
    text-shadow: 0 1px 1px rgba(0,0,0,0.18);
  }
  .tea-name-frame .placeholder-text { font-size: 26px; }
  .weight { position: absolute; left: 0; right: 0; top: 394px; text-align: center; font-size: 14px; }

  .description-box {
    position: absolute; left: 0; top: 200px; width: 210px; height: 175px;
    background: var(--leaf-green);
    display: flex; flex-direction: column; align-items: center; justify-content: center; gap: 10px;
  }
  .description-box .placeholder-text { font-size: 18px; letter-spacing: 5px; }

  .nutrition {
    position: absolute; left: 255px; top: 82px; width: 150px;
    background: var(--paper); border: 1px solid var(--ink); padding: 3px 4px 4px;
    font-family: "Libre Franklin", sans-serif; color: var(--ink); font-size: 7px; line-height: 1.3;
  }
  .nutrition h2 { font-weight: 900; font-size: 15px; line-height: 1; border-bottom: 1px solid var(--ink); padding-bottom: 2px; }
  .nutrition .row { display: flex; justify-content: space-between; border-bottom: 0.5px solid #555; }
  .nutrition .row.plain { border-bottom: none; }
  .nutrition .bar-thick { height: 5px; background: var(--ink); margin: 1px 0; }
  .nutrition .bar-mid { height: 2.5px; background: var(--ink); margin: 1px 0; }
  .nutrition .calories { display: flex; justify-content: space-between; align-items: flex-end; font-weight: 900; font-size: 12px; line-height: 1; }
  .nutrition .calories .value { font-size: 16px; }
  .nutrition .dv { text-align: right; font-size: 5px; border-bottom: 0.5px solid #555; }
  .nutrition .indent { padding-left: 8px; }
  .nutrition .indent-2 { padding-left: 16px; }
  .nutrition b { font-weight: 800; }
  .nutrition .footnote { font-size: 4.5px; line-height: 1.3; padding-top: 2px; }
</style>
</head>
<body>

<section class="label label--front">
  <div class="leaf-decor" role="img" aria-label="Faint outlined leaf decoration"></div>
  <div class="pennant"><span class="brand-name">Verdale</span></div>
  <div class="emblem" role="img" aria-label="Leaf emblem"></div>
  <div class="type-band">
    <span class="type-name">ARTISAN</span>
    <span class="type-sub">tea</span>
  </div>
  <div class="tea-name-frame"><span class="placeholder-text">text here</span></div>
  <p class="weight placeholder-text">weight</p>
</section>

<section class="label label--back">
  <div class="leaf-decor" role="img" aria-label="Faint outlined leaf decoration"></div>
  <div class="pennant"><span class="brand-name">Verdale</span></div>
  <div class="emblem" role="img" aria-label="Leaf emblem"></div>
  <div class="description-box">
    <span class="placeholder-text">Description</span>
    <span class="placeholder-text">text here</span>
  </div>
  <div class="type-band">
    <span class="type-name">ARTISAN</span>
    <span class="type-sub">tea</span>
  </div>

  <div class="nutrition">
    <h2>Nutrition Facts</h2>
    <div class="row plain">0 servings per container</div>
    <div class="row plain"><b>Serving size</b><b>0/0 cup (0g)</b></div>
    <div class="bar-thick"></div>
    <div class="row plain" style="font-size:5.5px"><b>Amount per serving</b></div>
    <div class="calories"><span>Calories</span><span class="value">0</span></div>
    <div class="bar-mid"></div>
    <div class="dv">% Daily Value*</div>
    <div class="row"><span><b>Total Fat</b> 0g</span><b>0%</b></div>
    <div class="row indent"><span>Saturated Fat 0g</span><b>0%</b></div>
    <div class="row indent"><span><i>Trans</i> Fat 0g</span></div>
    <div class="row indent"><span>Polyunsaturated Fat 0g</span></div>
    <div class="row indent"><span>Monounsaturated Fat 0g</span></div>
    <div class="row"><span><b>Cholesterol</b> 0mg</span><b>0%</b></div>
    <div class="row"><span><b>Sodium</b> 0mg</span><b>0%</b></div>
    <div class="row"><span><b>Total Carbohydrate</b> 0g</span><b>0%</b></div>
    <div class="row indent"><span>Dietary Fiber 0g</span><b>0%</b></div>
    <div class="row indent"><span>Total Sugars 0g</span></div>
    <div class="row indent-2"><span>Includes 0g Added Sugars</span><b>0%</b></div>
    <div class="row plain"><span><b>Protein</b> 0g</span></div>
    <div class="bar-thick"></div>
    <div class="row"><span>Vitamin D 0mcg</span><span>0%</span></div>
    <div class="row"><span>Calcium 0mg</span><span>0%</span></div>
    <div class="row"><span>Iron 0mg</span><span>0%</span></div>
    <div class="row"><span>Potassium 0mg</span><span>0%</span></div>
    <p class="footnote">* The % Daily Value (DV) tells you how much a nutrient in a serving of food adds to a daily diet. 2,000 calories a day is used for general advice.</p>
  </div>
</section>

</body>
</html>
```